interior designer/stylist looking for a letter press business card to reflect the stylish work

Hello Designers,
I need a business card design for an company called Halvard Interior Design. I'm aiming at the high end residential and private client market in London providing sleek simple interiors. I'd like my business card to be tackboard worthy and expensive looking, i want people to pin it and for it to have a sought after look, and want prospective customers to hire me as their interior designer as my card is so beautiful.
I love letter press design. I also like the use of colour/foil on the edge.
Colour combos & general things I like -
Black and White
Navy Blue and Gold
Neutral colours (muted palette of greys whites navys beiges)
White Marble & brass
Morvane (fashion designer)
....also open to other suggestions....
Please dont take the pink in the attached photos too literally. i'd like the card to look more masculine than feminine.
I'd like Halvard on one side in one font, with interior design underneath so one word will make the statement....... unless anyone has any other ideas, open to suggestions.
I'd like a really simple font and for the whole card to look very graphic.
my details -
Petra Quillby
Interior Designer & Stylist
email petra@halvardinteriordesign.co.uk
phone +447813554019
website wwww.halvardinteriordesign.co.uk
GO GO GO!! EXCITED TO SEE THE OUTCOME!!
x L
Target Market(s)
High End Residential and private clients
Industry/Entity Type
Business
Contact Information for Business Card
Halvard Interior Design & Styling
Petra Quillby
phone +447813554019

```html
<!DOCTYPE html>
<html lang="en">
<head>
<meta charset="utf-8">
<title>Halvard Interior Design — Business Card</title>
<link rel="stylesheet" href="https://fonts.googleapis.com/css2?family=Jost:wght@400&display=swap">
<style>
  :root {
    --card-white: #ffffff;
    --ink: #3d3d3d;
    --gold-light: #f3d98a;
    --gold-mid: #dcb453;
    --gold-deep: #c39a3a;
    --frame-width: 11px;
  }
  html, body {
    margin: 0;
    padding: 0;
    width: 1200px;
    height: 686px;
    overflow: hidden;
    background: var(--card-white);
  }
  .card {
    position: relative;
    width: 1200px;
    height: 686px;
    box-sizing: border-box;
    background: var(--card-white);
    font-family: "Jost", sans-serif;
    color: var(--ink);
    display: flex;
    align-items: center;
    justify-content: center;
  }
  .foil-edge {
    position: absolute;
    inset: 0;
    border: var(--frame-width) solid transparent;
    border-image: linear-gradient(120deg,
      var(--gold-mid) 0%, var(--gold-light) 18%, var(--gold-deep) 38%,
      var(--gold-light) 55%, var(--gold-mid) 72%, var(--gold-deep) 88%,
      var(--gold-light) 100%) 1;
    pointer-events: none;
  }
  .business-name {
    margin: 0;
    font-weight: 400;
    font-size: 44px;
    line-height: 1;
    letter-spacing: 0.2em;
    padding-left: 0.2em;
    white-space: nowrap;
    text-align: center;
  }
</style>
</head>
<body>
  <div class="card">
    <h1 class="business-name">HALVARD INTERIOR DESIGN</h1>
    <div class="foil-edge"></div>
  </div>
</body>
</html>
```